依頼詳細
会社の名刺デザインを新しくしたいと思っています。
リフォーム業のため、「シンプル」だけど「高級感のある」デザインを希望します。
名刺の背景は白地となります。
記載項目

表面:会社名/役職/住所/電話/Fax/Mail
裏面:無地
希望イメージ
シンプル 複雑
単色 カラフル
暗い 明るい
日常 高級
遊び心 厳粛
未来的 伝統的
女性的 男性的
希望する色
青、黄緑
納品ファイル
• 高解像度JPG (.jpg)
• イラストレーター形式 (.ai)
補足説明
■ 選んだ理由

デザインが良かったです。

■ 提案者全員のお礼・コメント

素晴らしい提案ありがとうございました。

また何か依頼する時は、よろしくお願いします。

```html
<!DOCTYPE html>
<html lang="ja">
<head>
<meta charset="utf-8">
<title>アオゾラホーム 名刺</title>
<link rel="stylesheet" href="https://fonts.googleapis.com/css2?family=Noto+Sans+JP:wght@400;500;700&display=swap">
<style>
  :root {
    --paper: #ffffff;
    --ink: #1a1a1a;
    --brand: #5f7f8f;
    --mark: #2f8fc9;
    --sea-top: #dcebf8;
    --sea-mid: #a4cbea;
    --sea-deep: #6aa6d8;
    --crop: #222222;
  }
  html, body {
    margin: 0;
    padding: 0;
    width: 831px;
    height: 1200px;
    overflow: hidden;
    background: var(--paper);
  }
  .sheet {
    position: relative;
    width: 831px;
    height: 1200px;
    font-family: "Noto Sans JP", sans-serif;
    color: var(--ink);
  }
  .crop-marks {
    position: absolute;
    inset: 0;
  }
  .sea-panel {
    position: absolute;
    left: 117px;
    top: 730px;
    width: 610px;
    height: 410px;
    background: linear-gradient(to bottom, var(--sea-top) 0%, var(--sea-mid) 40%, var(--sea-deep) 100%);
  }
  .brand {
    position: absolute;
    left: 117px;
    width: 610px;
    top: 214px;
    text-align: center;
  }
  .brand__dot {
    width: 90px;
    height: 90px;
    margin: 0 auto 24px;
    border-radius: 50%;
    background: var(--mark);
  }
  .brand__name {
    font-size: 56px;
    font-weight: 400;
    color: var(--brand);
    letter-spacing: 1px;
    line-height: 1;
  }
  .person {
    position: absolute;
    left: 178px;
    top: 456px;
  }
  .person__title {
    font-size: 27px;
    font-weight: 500;
    line-height: 1;
    margin: 0 0 22px;
  }
  .person__name {
    font-size: 50px;
    font-weight: 700;
    line-height: 1;
    margin: 0 0 16px;
    letter-spacing: 2px;
  }
  .person__roman {
    font-size: 24px;
    font-weight: 400;
    line-height: 1;
    margin: 0;
  }
  .company {
    position: absolute;
    left: 117px;
    width: 610px;
    top: 812px;
    color: #ffffff;
  }
  .company__name {
    text-align: center;
    font-size: 30px;
    font-weight: 700;
    margin: 0 0 26px;
    line-height: 1;
  }
  .company__details {
    margin: 0 0 0 38px;
    font-size: 20px;
    line-height: 50px;
    font-style: normal;
  }
  .company__details span { display: block; white-space: nowrap; }
</style>
</head>
<body>
<main class="sheet">
  <div class="sea-panel" role="img" aria-label="淡い青の水面と泡の装飾エリア"></div>

  <svg class="crop-marks" width="831" height="1200" viewBox="0 0 831 1200" aria-hidden="true">
    <g stroke="var(--crop)" stroke-width="1.5" fill="none">
      <path d="M117 0 V40 M95 0 V60 M0 60 H97 M0 38 H117"/>
      <path d="M727 0 V40 M749 0 V60 M831 60 H747 M831 38 H727"/>
      <path d="M117 1200 V1160 M95 1200 V1140 M0 1140 H97 M0 1162 H117"/>
      <path d="M727 1200 V1160 M749 1200 V1140 M831 1140 H747 M831 1162 H727"/>
      <path d="M0 600 H60 M30 560 V640"/>
      <path d="M771 600 H831 M801 560 V640"/>
      <path d="M422 0 V30 M372 15 H472"/>
      <path d="M422 1170 V1200 M372 1185 H472"/>
    </g>
  </svg>

  <header class="brand">
    <div class="brand__dot"></div>
    <div class="brand__name">Aozora Home</div>
  </header>

  <section class="person">
    <p class="person__title">代表取締役</p>
    <p class="person__name">佐藤　健一</p>
    <p class="person__roman">KENICHI SATO</p>
  </section>

  <section class="company">
    <p class="company__name">株式会社アオゾラホーム</p>
    <address class="company__details">
      <span>〒135-0042</span>
      <span>東京都青葉区空見町 5-8 青空ビル 3 階</span>
      <span>Tel :03-5550-1234 Fax :03-5550-1235</span>
      <span>E mail:info@aozora-home.example</span>
    </address>
  </section>
</main>
</body>
</html>
```